Business Card Design Project

Hi,

We need new business cards for our company The Brightmere Trading
www.thebrightmeretrading.example

Clean design

We will be focussing a lot on social media and online business in 2013.

All our social media channels should be included
Trellisly Group or Trellisly Company Page ,Wavetome Page,Zentro and website

Mobile number, general telephone number,emailadress, street address etc

On the back of the card we want to promote our Velder Institute Coaching Workshops (we do this via our Plomvista page) with a place for a unique voucher code (reduction of 75 € for a coaching workshop of your choice) for every card

We would like to have our personal photo's in it.

Designs should be easy to adapt afterwards (when we hire new people - new pictures etc.)

We would like to work with Zel as business cards service

Target Market(s)

All B2B Professionals

Industry/Entity Type

Business

Requirements
Nice to have
• QR code?

```html
<!DOCTYPE html>
<html lang="en">
<head>
<meta charset="utf-8">
<title>The Brightmere Trading – Business Card</title>
<link rel="stylesheet" href="https://fonts.googleapis.com/css2?family=Exo+2:wght@700;800&family=Open+Sans:wght@600;700&display=swap">
<style>
  :root {
    --page-bg: #e9ebee;
    --blue-deep: #163f94;
    --blue-mid: #1f63c4;
    --blue-bright: #2f8fe2;
    --cyan-band: #36a8ea;
    --navy-text: #1a3b95;
    --white: #ffffff;
    --soft-white: #dfeafb;
    --placeholder: #c9a48a;
  }
  * { box-sizing: border-box; margin: 0; padding: 0; }
  html, body { width: 1067px; height: 1200px; overflow: hidden; }
  body {
    background: var(--page-bg);
    font-family: "Open Sans", Arial, sans-serif;
    position: relative;
  }
  .card {
    position: absolute;
    left: 103px;
    width: 860px;
    height: 490px;
    border-radius: 4px;
    overflow: hidden;
    box-shadow: 0 8px 24px rgba(20, 40, 80, 0.25);
  }
  .card-front { top: 70px; }
  .card-back { top: 630px; }
  .card-shapes { position: absolute; inset: 0; width: 100%; height: 100%; }

  /* Front */
  .front-brand {
    position: absolute;
    left: 90px; top: 120px;
    display: flex; align-items: center; gap: 22px;
  }
  .brand-dot {
    width: 78px; height: 78px; border-radius: 50%;
    background: var(--soft-white);
    flex: none;
  }
  .front-brand .brand-name {
    font-family: "Exo 2", Arial, sans-serif;
    font-weight: 800;
    font-size: 54px;
    line-height: 1.0;
    color: var(--white);
  }
  .social-row {
    position: absolute;
    left: 40px; right: 40px; top: 324px;
    display: flex; justify-content: center; gap: 20px;
    color: var(--white);
    font-size: 12.5px; font-weight: 700;
  }
  .social-item { display: flex; align-items: center; gap: 6px; white-space: nowrap; }
  .social-square { width: 13px; height: 13px; background: var(--white); flex: none; }
  .social-name { opacity: 0.85; }

  /* Back */
  .back-brand {
    position: absolute;
    left: 0; right: 0; top: 32px;
    display: flex; flex-direction: column; align-items: center; gap: 10px;
  }
  .back-brand .brand-dot { width: 46px; height: 46px; background: var(--blue-mid); }
  .back-brand .brand-name {
    font-family: "Exo 2", Arial, sans-serif;
    font-weight: 800;
    font-size: 36px;
    color: var(--navy-text);
  }
  .person {
    position: absolute;
    left: 90px; top: 238px;
    width: 250px;
    text-align: center;
  }
  .person-photo {
    display: block;
    width: 108px; height: 118px;
    margin: 0 auto 12px;
    border: 4px solid var(--white);
    background: linear-gradient(160deg, #e2c3a8, var(--placeholder) 60%, #8c5a3c);
  }
  .person-name {
    font-family: "Exo 2", Arial, sans-serif;
    font-weight: 800; font-size: 19px;
    color: var(--navy-text);
    letter-spacing: 0.5px;
    white-space: nowrap;
  }
  .person-role { color: var(--white); font-size: 14px; font-weight: 700; text-align: right; padding-right: 30px; }
  .divider {
    position: absolute;
    left: 360px; top: 235px;
    width: 1px; height: 200px;
    background: rgba(255, 255, 255, 0.45);
  }
  .contact {
    position: absolute;
    left: 390px; top: 238px;
    color: var(--white);
    font-size: 15.5px; font-weight: 700;
    line-height: 1.35;
  }
  .contact-address { margin-bottom: 18px; }
  .contact-list { list-style: none; }
  .contact-list li { display: flex; align-items: center; gap: 10px; }
  .contact-icon { width: 16px; height: 16px; flex: none; }
</style>
</head>
<body>

<section class="card card-front" aria-label="Card front">
  <svg class="card-shapes" viewBox="0 0 860 490" preserveAspectRatio="none" aria-hidden="true">
    <defs>
      <radialGradient id="frontGlow" cx="0.62" cy="0.45" r="0.75">
        <stop offset="0" stop-color="#3aa0ee"/>
        <stop offset="0.55" stop-color="#1f63c4"/>
        <stop offset="1" stop-color="#163f94"/>
      </radialGradient>
    </defs>
    <rect width="860" height="490" fill="url(#frontGlow)"/>
    <circle cx="640" cy="220" r="150" fill="none" stroke="#1b4ea8" stroke-width="50" opacity="0.45"/>
    <path d="M0 395 Q420 420 860 330 L860 490 L0 490 Z" fill="#36a8ea"/>
    <path d="M0 395 Q420 420 860 330 L860 345 Q420 432 0 410 Z" fill="#1f63c4" opacity="0.5"/>
  </svg>
  <div class="front-brand">
    <span class="brand-dot"></span>
    <span class="brand-name">The Brightmere<br>Trading</span>
  </div>
  <div class="social-row">
    <span class="social-item"><span class="social-square"></span><span class="social-name">Trellisly</span> /company/brightmere-trading</span>
    <span class="social-item"><span class="social-square"></span><span class="social-name">Wavetome</span> /brightmeretrading</span>
    <span class="social-item"><span class="social-square"></span><span class="social-name">Zentro</span> /brightmeretrading</span>
  </div>
</section>

<section class="card card-back" aria-label="Card back">
  <svg class="card-shapes" viewBox="0 0 860 490" preserveAspectRatio="none" aria-hidden="true">
    <defs>
      <radialGradient id="backGlow" cx="0.6" cy="0.7" r="0.8">
        <stop offset="0" stop-color="#2f8fe2"/>
        <stop offset="0.6" stop-color="#1f5dbd"/>
        <stop offset="1" stop-color="#163f94"/>
      </radialGradient>
    </defs>
    <rect width="860" height="490" fill="#ffffff"/>
    <circle cx="110" cy="110" r="80" fill="none" stroke="#e1e2e4" stroke-width="34"/>
    <path d="M0 205 Q430 215 860 120 L860 490 L0 490 Z" fill="#36a8ea"/>
    <path d="M0 218 Q430 228 860 134 L860 490 L0 490 Z" fill="url(#backGlow)"/>
  </svg>
  <div class="back-brand">
    <span class="brand-dot"></span>
    <span class="brand-name">The Brightmere Trading</span>
  </div>
  <div class="person">
    <span class="person-photo" role="img" aria-label="Portrait photo of the card holder"></span>
    <div class="person-name">MARTEN HOLLOWAY</div>
    <div class="person-role">Manager</div>
  </div>
  <div class="divider"></div>
  <div class="contact">
    <p class="contact-address">Lindenlaan 14, 4120 Varenmoor<br>(Coastal Area), Nordland</p>
    <ul class="contact-list">
      <li>
        <svg class="contact-icon" viewBox="0 0 16 16" aria-hidden="true"><path d="M3 1h3l1.5 4-2 1.2a9 9 0 0 0 4.3 4.3L11 8.5l4 1.5v3a2 2 0 0 1-2 2A12 12 0 0 1 1 3a2 2 0 0 1 2-2z" fill="#fff"/></svg>
        + 00 5550 1427 3380
      </li>
      <li>
        <svg class="contact-icon" viewBox="0 0 16 16" aria-hidden="true"><rect x="4" y="1" width="8" height="14" rx="1.5" fill="none" stroke="#fff" stroke-width="1.6"/><circle cx="8" cy="12.5" r="0.9" fill="#fff"/></svg>
        + 00 5550 1427 3381
      </li>
      <li>
        <svg class="contact-icon" viewBox="0 0 16 16" aria-hidden="true"><rect x="1" y="3" width="14" height="10" fill="#fff"/><path d="M1 3l7 6 7-6" fill="none" stroke="#1f5dbd" stroke-width="1.4"/></svg>
        info@thebrightmeretrading.example
      </li>
      <li>
        <svg class="contact-icon" viewBox="0 0 16 16" aria-hidden="true"><circle cx="8" cy="8" r="6.5" fill="none" stroke="#fff" stroke-width="1.5"/><path d="M1.5 8h13M8 1.5c-3 3.5-3 9.5 0 13M8 1.5c3 3.5 3 9.5 0 13" fill="none" stroke="#fff" stroke-width="1.2"/></svg>
        www.thebrightmeretrading.example
      </li>
    </ul>
  </div>
</section>

</body>
</html>
```